beauty salon

providing waxing services from a home base this must include which I will provide a price list and an address

Industry/Entity Type

Beauty Salon

Font styles to use
Script

Colors

Designer to choose colors to be used in the design.

```html
<!DOCTYPE html>
<html lang="en">
<head>
<meta charset="utf-8">
<title>Maren's Garden Salon – Waxing Price List</title>
<link rel="stylesheet" href="https://fonts.googleapis.com/css2?family=Bitter:ital,wght@1,700&family=Open+Sans:ital,wght@0,300;0,700;1,700&family=Arimo&display=swap">
<style>
  :root {
    --page: #e4e2ea;
    --flyer: #cdcbdd;
    --plum: #7a1f63;
    --navy: #2c2b68;
    --mauve: #7a6790;
    --ink: #2b2b2b;
    --grey: #444;
    --red: #e5232b;
    --fold: #1e1e1e;
    --white: #fff;
  }
  * { box-sizing: border-box; margin: 0; padding: 0; }
  html, body { width: 1200px; height: 872px; overflow: hidden; background: var(--page); }
  .flyer {
    position: absolute; left: 35px; top: 35px; width: 1130px; height: 800px;
    background: var(--flyer);
  }
  .abs { position: absolute; }

  .brand {
    left: 88px; top: 110px; width: 420px; display: flex; align-items: center; justify-content: center; gap: 12px;
    font-family: "Open Sans", sans-serif; font-weight: 700; font-size: 30px; color: var(--plum); white-space: nowrap;
  }
  .brand-dot { width: 14px; height: 14px; border-radius: 50%; background: var(--plum); }

  .credential {
    left: 64px; top: 158px; font-family: "Open Sans", sans-serif; font-weight: 700; font-style: italic;
    font-size: 19px; color: var(--ink); white-space: nowrap;
  }
  .credential strong { font-size: 27px; }

  .photo {
    left: 0; top: 200px; width: 587px; height: 393px;
    background: linear-gradient(120deg, #f3efea 0%, #e9d2b8 35%, #f6f1ec 60%, #d9c2a4 100%);
  }

  .offer {
    left: 610px; top: 22px; width: 500px; text-align: center;
    font-family: "Bitter", serif; font-style: italic; font-weight: 700; color: var(--plum); line-height: 1.1;
  }
  .offer .big { font-size: 52px; }
  .offer .mid { font-size: 35px; }
  .offer .line2 { display: block; font-size: 38px; margin-top: 2px; }

  .folds { left: 0; top: 0; width: 1130px; height: 800px; }

  .prices {
    left: 587px; top: 155px; width: 543px; height: 442px; background: var(--red); color: var(--white);
  }
  .price-col { position: absolute; }
  .col-lady { left: 18px; top: 18px; width: 229px; }
  .col-men { left: 286px; top: 18px; width: 230px; }
  .price-heading {
    font-family: "Bitter", serif; font-style: italic; font-weight: 700; font-size: 21px;
    text-align: center; margin-bottom: 6px;
  }
  .price-list { list-style: none; font-family: "Arimo", sans-serif; font-size: 15px; }
  .price-list li { display: flex; align-items: baseline; white-space: nowrap; }
  .col-lady .price-list li { height: 24px; }
  .col-men .price-list li { height: 33.5px; }
  .price-list .dots { flex: 1; overflow: hidden; }
  .price-list .dots::after { content: "......................................................................"; }
  .col-men .sub { margin-top: 2px; }

  .hours {
    left: 60px; top: 610px; width: 460px; text-align: center;
    font-family: "Bitter", serif; font-style: italic; font-weight: 700; font-size: 31px; line-height: 44px;
  }
  .hours .label { color: var(--mauve); }
  .hours .day { color: var(--navy); font-size: 33px; }
  .hours .time { color: var(--mauve); }

  .contact { left: 610px; top: 622px; width: 480px; text-align: center; }
  .phone {
    font-family: "Open Sans", sans-serif; font-weight: 700; font-style: italic; font-size: 42px; color: #3a3a3a;
  }
  .address {
    font-family: "Open Sans", sans-serif; font-weight: 300; font-size: 47px; color: var(--grey); line-height: 54px;
  }
</style>
</head>
<body>
<div class="flyer">
  <div class="abs brand"><span class="brand-dot"></span>Maren's Garden Salon</div>
  <div class="abs credential">Diploma of Beauty Therapy&nbsp; At <strong>Tessa Marlow</strong></div>

  <div class="abs photo" role="img" aria-label="Photo of a woman receiving a facial mask treatment with cucumber slices over her eyes"></div>

  <div class="abs offer">
    <span class="big">10% Off</span> <span class="mid">&nbsp;discount on</span>
    <span class="line2">first treatment</span>
  </div>

  <svg class="abs folds" viewBox="0 0 1130 800" aria-hidden="true">
    <polygon points="555,200 587,155 587,200" fill="var(--fold)"/>
    <polygon points="587,597 635,597 635,630" fill="var(--fold)"/>
  </svg>

  <section class="abs prices">
    <div class="price-col col-lady">
      <h2 class="price-heading">Lady’s Waxing</h2>
      <ul class="price-list">
        <li>Eyebrow<span class="dots"></span>$8</li>
        <li>Upper lip<span class="dots"></span>$8</li>
        <li>Chin<span class="dots"></span>$8</li>
        <li>Face wax<span class="dots"></span>$25</li>
        <li>Bikini line<span class="dots"></span>$15</li>
        <li>G string<span class="dots"></span>$20</li>
        <li>½ Brazilian<span class="dots"></span>$30</li>
        <li>Full Brazilian<span class="dots"></span>$40</li>
        <li>Half arm<span class="dots"></span>$20</li>
        <li>Upper half arm<span class="dots"></span>$20</li>
        <li>Full arm<span class="dots"></span>$25</li>
        <li>Half leg<span class="dots"></span>$15</li>
        <li>Upper leg<span class="dots"></span>$20</li>
        <li>¾ Leg<span class="dots"></span>$25</li>
        <li>Full leg<span class="dots"></span>$35</li>
      </ul>
    </div>
    <div class="price-col col-men">
      <h2 class="price-heading">Men’s Waxing</h2>
      <ul class="price-list">
        <li>Eyebrow<span class="dots"></span>$10</li>
        <li>Half arm<span class="dots"></span>$20</li>
        <li>Upper half arm<span class="dots"></span>$25</li>
        <li>Full arm<span class="dots"></span>$30</li>
        <li>Half leg<span class="dots"></span>$25</li>
        <li>Full leg<span class="dots"></span>$45</li>
        <li>Chest wax<span class="dots"></span>$40</li>
        <li>Back wax<span class="dots"></span>$35</li>
      </ul>
      <h2 class="price-heading sub">Eye Enhancement</h2>
      <ul class="price-list">
        <li>Eyebrow tint<span class="dots"></span>$12</li>
        <li>Eyelash tint<span class="dots"></span>$15</li>
      </ul>
    </div>
  </section>

  <div class="abs hours">
    <div class="label">Now open:</div>
    <div><span class="day">Wednesday</span> <span class="time">10am – 4pm</span></div>
    <div><span class="day">Fridays</span> <span class="time">10am-7pm</span></div>
    <div><span class="day">Saturday</span> <span class="time">10am - 4pm</span></div>
  </div>

  <div class="abs contact">
    <div class="phone">Call us&nbsp; 0455 318 276</div>
    <div class="address">12 Finch Lane North<br>Ashvale</div>
  </div>
</div>
</body>
</html>
```